Our new all natural drink needs a product design (logo and front-pack).
We developed an innovative alternative under the brand name "7 Ways to Sip" - all natural and great tasting soft drink and ice tea, beyond the conventional big commercial brands. Our ambition is to set a new high standard for soft drinks and ice tea, produced in a simple honest manner.

Target Market(s)

European markets

Colors

Designer to choose colors to be used in the design.

Requirements
Must have
• We want “clean” minimalist design with focus on the number “1”, but also to present the ingredients we have inside the different flavor variants (see the brief attached)
• We also want to be visible and easy recognizable on the shelves in-store
Nice to have
• Product benefits: 100% natural products. No white sugar, aromas, colors, additives, artificial substances, citric acids or ascorbic acids allowed.
• We focus on the highest quality possible and superior natural taste experiences. In general, no compromises!
Should not have
• Must not be overcrowded and with too much colors. Must not have similarities with the conventional big commercial brands (e.g. Vorla Brim, Zunto, etc.)

```html
<!DOCTYPE html>
<html lang="en">
<head>
<meta charset="utf-8">
<title>7 Ways to Sip — Front Pack Labels</title>
<link href="https://fonts.googleapis.com/css2?family=Archivo:wght@700;800&display=swap" rel="stylesheet">
<style>
  :root {
    --page-bg: #eceef1;
    --white: #ffffff;
    --citrus-fill-top: #ffc928;
    --citrus-fill-bottom: #f6a90c;
    --citrus-accent: #e8b800;
    --citrus-rule: #ffe51f;
    --berry-fill-top: #c4c7cc;
    --berry-fill-bottom: #a9adb3;
    --berry-accent: #9b1a62;
    --berry-icon: #c2185b;
  }
  * { box-sizing: border-box; margin: 0; padding: 0; }
  html, body {
    width: 1200px;
    height: 1007px;
    overflow: hidden;
    background: var(--page-bg);
    font-family: "Archivo", "Arial Narrow", sans-serif;
  }
  .shelf {
    width: 1200px;
    height: 1007px;
    display: flex;
    justify-content: center;
    align-items: center;
    gap: 120px;
  }
  .label {
    position: relative;
    width: 440px;
    height: 800px;
    border-radius: 28px;
    overflow: hidden;
  }
  .label--citrus { background: linear-gradient(180deg, var(--citrus-fill-top), var(--citrus-fill-bottom)); --accent: var(--citrus-accent); --rule: var(--citrus-rule); --icon: var(--citrus-rule); }
  .label--berry { background: linear-gradient(180deg, var(--berry-fill-top), var(--berry-fill-bottom)); --accent: var(--berry-accent); --rule: var(--berry-accent); --icon: var(--berry-icon); }

  .brand {
    position: absolute;
    top: 150px;
    left: 0; right: 0;
    display: flex;
    justify-content: center;
    align-items: center;
    gap: 10px;
    color: var(--white);
    font-weight: 800;
    font-size: 26px;
    letter-spacing: 0.5px;
    text-transform: uppercase;
  }
  .brand-mark {
    width: 30px;
    height: 30px;
    background: var(--white);
  }

  .rule {
    position: absolute;
    left: 0; right: 0;
    height: 6px;
    background: var(--rule);
  }
  .rule--top { top: 240px; }
  .rule--bottom { top: 640px; }

  .benefits {
    position: absolute;
    left: 40px; right: 40px;
    display: flex;
    flex-direction: column;
    align-items: center;
    gap: 8px;
    color: var(--white);
    font-weight: 700;
    line-height: 1.1;
    text-align: center;
  }
  .benefits--upper { top: 268px; }
  .benefits--lower { top: 478px; }
  .benefit-major { font-size: 22px; }
  .benefit-minor { font-size: 14px; text-transform: uppercase; letter-spacing: 1.5px; }

  .flavour {
    position: absolute;
    top: 415px;
    left: 50%;
    width: 360px;
    height: 44px;
    margin-left: -180px;
    background: var(--white);
    border-radius: 6px;
    display: flex;
    justify-content: center;
    align-items: center;
    color: var(--accent);
    font-weight: 800;
    font-size: 21px;
  }
  .flavour-icon {
    position: absolute;
    top: -16px;
    left: 50%;
    width: 30px;
    height: 30px;
    margin-left: -15px;
    border-radius: 50%;
    background: var(--white);
    border: 3px solid var(--icon);
  }
</style>
</head>
<body>
<main class="shelf">

  <article class="label label--citrus">
    <div class="brand"><span class="brand-mark"></span><span class="brand-name">7 Ways to Sip</span></div>
    <div class="rule rule--top"></div>
    <div class="benefits benefits--upper">
      <span class="benefit-major">simply pure</span>
      <span class="benefit-minor">no white sugar</span>
      <span class="benefit-major">grown close to home</span>
      <span class="benefit-minor">no added colours</span>
    </div>
    <div class="flavour">
      <span class="flavour-icon" role="img" aria-label="Small citrus icon"></span>
      Citrus with Mountain Mint
    </div>
    <div class="benefits benefits--lower">
      <span class="benefit-minor">no additives</span>
      <span class="benefit-major">bright and crisp</span>
      <span class="benefit-minor">honest ingredients</span>
      <span class="benefit-major">gently made</span>
    </div>
    <div class="rule rule--bottom"></div>
  </article>

  <article class="label label--berry">
    <div class="brand"><span class="brand-mark"></span><span class="brand-name">7 Ways to Sip</span></div>
    <div class="rule rule--top"></div>
    <div class="benefits benefits--upper">
      <span class="benefit-major">simply pure</span>
      <span class="benefit-minor">no white sugar</span>
      <span class="benefit-major">grown close to home</span>
      <span class="benefit-minor">no added colours</span>
    </div>
    <div class="flavour">
      <span class="flavour-icon" role="img" aria-label="Small berry icon"></span>
      Wild Berries with Hibiscus
    </div>
    <div class="benefits benefits--lower">
      <span class="benefit-minor">no additives</span>
      <span class="benefit-major">bright and crisp</span>
      <span class="benefit-minor">honest ingredients</span>
      <span class="benefit-major">gently made</span>
    </div>
    <div class="rule rule--bottom"></div>
  </article>

</main>
</body>
</html>
```